Reed & Vale NC grand opening (for BILLBOARD)

Advertising the grand opening of our cannabis/hemp shop in NC. We will sell all things hemp (flower, cartridges, disposables, edibles, creams, lotions, pet products etc...)

Requirements
Must have
• include, open starting Aug 1, but grand opening Aug 15th.
Nice to have
• Difference slogan ideas "Save some cash, buy our grass" "Find your perfect high at Reed & Vale cannabis store" "Experience Nature's Gift: Reed & Vale Cannabis Store"

```html
<!DOCTYPE html>
<html lang="en">
<head>
<meta charset="UTF-8">
<title>Reed &amp; Vale — Grand Opening Billboard</title>
<link href="https://fonts.googleapis.com/css2?family=Montserrat:wght@500;700&family=Fredoka:wght@600&family=Playfair+Display:wght@900&family=Roboto+Condensed:wght@500;700&display=swap" rel="stylesheet">
<style>
  :root {
    --page: #e9ebea;
    --board: #12673f;
    --board-deep: #0e5a36;
    --lime: #7ac143;
    --white: #ffffff;
    --ink: #0f4d2f;
  }
  * { margin: 0; padding: 0; box-sizing: border-box; }
  html, body {
    width: 1200px; height: 962px; overflow: hidden;
    background: var(--page);
  }
  .billboard {
    position: absolute; left: 0; top: 151px;
    width: 1200px; height: 660px;
    background: radial-gradient(ellipse at 50% 45%, var(--board) 55%, var(--board-deep) 100%);
    overflow: hidden;
  }
  .leaf-texture {
    position: absolute; inset: 0;
    background: linear-gradient(135deg, rgba(255,255,255,0.02), rgba(0,0,0,0.05));
  }
  .brand {
    position: absolute; left: 0; width: 1200px; top: 95px;
    text-align: center;
    font-family: "Montserrat", sans-serif; font-weight: 700;
    font-size: 124px; line-height: 1; letter-spacing: -3px;
    color: var(--white);
  }
  .slogan {
    position: absolute; left: 215px; top: 282px;
    width: 720px; height: 58px;
    border: 2px solid var(--lime); border-radius: 29px;
    display: flex; align-items: center; justify-content: center;
    font-family: "Fredoka", sans-serif; font-weight: 600;
    font-size: 36px; text-transform: uppercase; color: var(--lime);
    letter-spacing: 0.5px;
  }
  .grand {
    position: absolute; left: 0; width: 1130px; top: 372px;
    text-align: center;
    font-family: "Montserrat", sans-serif; font-weight: 500;
    font-size: 18px; letter-spacing: 18px; color: var(--white);
  }
  .opening {
    position: absolute; left: 0; width: 1130px; top: 395px;
    text-align: center;
    font-family: "Playfair Display", serif; font-weight: 900;
    font-size: 92px; letter-spacing: 16px; line-height: 1; color: var(--lime);
  }
  .date-tag {
    position: absolute; left: 462px; top: 478px;
    width: 206px; height: 72px;
    background: var(--white);
    transform: rotate(-10deg);
    box-shadow: 3px 4px 0 rgba(0,0,0,0.15);
    display: flex; flex-direction: column; align-items: center; justify-content: center;
    font-family: "Roboto Condensed", sans-serif; font-weight: 700;
    font-size: 30px; color: var(--ink); line-height: 1;
  }
  .date-tag sup { font-size: 14px; vertical-align: 12px; margin-right: 4px; }
  .date-tag svg { margin-top: 6px; }
  .footer-rule {
    position: absolute; left: 0; right: 0; top: 590px;
    height: 2px; background: var(--lime);
  }
  .soft-open {
    position: absolute; left: 300px; top: 568px;
    width: 300px; height: 46px; border-radius: 23px;
    background: var(--lime);
    display: flex; align-items: center; justify-content: center;
    font-family: "Roboto Condensed", sans-serif; font-weight: 500;
    font-size: 28px; color: var(--white);
  }
  .soft-open sup { font-size: 15px; vertical-align: 12px; }
</style>
</head>
<body>
  <section class="billboard">
    <div class="leaf-texture" role="img" aria-label="Faint pattern of large green leaves across the background"></div>

    <h1 class="brand">Reed &amp; Vale</h1>

    <p class="slogan">Save some cash, buy our grass</p>

    <p class="grand">GRAND</p>
    <p class="opening">OPENING</p>

    <div class="date-tag">
      <span>15<sup>TH</sup>AUGUST</span>
      <svg width="140" height="10" viewBox="0 0 140 10" aria-hidden="true">
        <path d="M2 7 Q70 1 138 3" stroke="#0f4d2f" stroke-width="1.5" fill="none"/>
        <path d="M12 9 Q70 4 128 6" stroke="#0f4d2f" stroke-width="1" fill="none"/>
      </svg>
    </div>

    <div class="footer-rule"></div>
    <p class="soft-open">Open Starting Aug 1<sup>st</sup></p>
  </section>
</body>
</html>
```